Beer Can Label named: ZOK Ginger Beer

We need a funky design for a Ginger Beer that is made from all natural ingredients. The label needs to be full of Colour, emphasis on the Ginger Root. ZOK (Zested Over Korvale)

Target Market(s)

None beer drinkers'

Requirements
Must have
• Name on the label must beer easy to read. Needs to be very colourful, playful & even a bit cheaky.
Nice to have
• A label that looks at the benefits of Ginger for the body in a fun artistic design.
Should not have
• Should NOT be a simple, basic, minimalistic design

```html
<!DOCTYPE html>
<html lang="en">
<head>
<meta charset="utf-8">
<title>ZOK Ginger Beer – Label Range</title>
<link rel="stylesheet" href="https://fonts.googleapis.com/css2?family=Patua+One&family=Signika:wght@400;600&display=swap">
<style>
  :root {
    --backdrop: #e2e0e0;
    --ink-white: #fbf8f2;
    --label-orange: #ee7a3a;
    --label-olive: #c2bd63;
    --label-brown: #9a6e54;
    --rule-white: #fdfaf4;
  }
  * { box-sizing: border-box; margin: 0; padding: 0; }
  html, body {
    width: 1200px;
    height: 900px;
    overflow: hidden;
    background: var(--backdrop);
  }
  .label-range {
    position: absolute;
    top: 200px;
    left: 80px;
    display: flex;
    gap: 40px;
  }
  .label {
    position: relative;
    width: 320px;
    height: 490px;
    background: var(--label-colour);
    color: var(--ink-white);
    text-align: center;
    overflow: hidden;
  }
  .label--orange { --label-colour: var(--label-orange); }
  .label--olive  { --label-colour: var(--label-olive); }
  .label--brown  { --label-colour: var(--label-brown); }

  .label__rules {
    position: absolute;
    left: 0; right: 0;
    height: 22px;
  }
  .label__rules::before,
  .label__rules::after {
    content: "";
    position: absolute;
    left: 0; right: 0;
    background: var(--rule-white);
  }
  .label__rules--top { top: 14px; }
  .label__rules--top::before { top: 0; height: 7px; }
  .label__rules--top::after  { top: 13px; height: 3px; }
  .label__rules--bottom { bottom: 14px; }
  .label__rules--bottom::before { bottom: 0; height: 7px; }
  .label__rules--bottom::after  { bottom: 13px; height: 3px; }

  .label__ginger-art {
    position: absolute;
    left: 40px;
    top: 70px;
    width: 260px;
    height: 260px;
    border-radius: 46% 54% 40% 60% / 50% 44% 56% 50%;
    background: radial-gradient(ellipse at 55% 45%, rgba(255,255,255,0.14), rgba(255,255,255,0) 70%);
  }

  .label__title {
    position: relative;
    margin-top: 52px;
    padding: 0 14px;
    font-family: "Patua One", serif;
    font-weight: 400;
    line-height: 1;
    letter-spacing: 0;
    text-transform: uppercase;
    white-space: nowrap;
  }
  .label__title span { display: block; }
  .title-top, .title-bottom { font-size: 88px; }
  .title-mid { font-size: 72px; margin: 4px 0; }

  .label__ribbon {
    position: relative;
    display: inline-block;
    margin-top: 34px;
    padding: 3px 16px;
    background: var(--ink-white);
    color: var(--label-colour);
    font-family: "Signika", sans-serif;
    font-weight: 600;
    font-size: 15px;
    letter-spacing: 1px;
    text-transform: uppercase;
    clip-path: polygon(0 0, 100% 0, 96% 50%, 100% 100%, 0 100%, 4% 50%);
  }
  .label__volume {
    position: relative;
    margin-top: 26px;
    font-family: "Signika", sans-serif;
    font-weight: 400;
    font-size: 17px;
    letter-spacing: 0.5px;
  }
</style>
</head>
<body>
  <main class="label-range">
    <section class="label label--orange">
      <div class="label__rules label__rules--top"></div>
      <div class="label__ginger-art" role="img" aria-label="Line illustration of a ginger root behind the name"></div>
      <h1 class="label__title"><span class="title-top">ZOK</span><span class="title-mid">Ginger</span><span class="title-bottom">Beer</span></h1>
      <p class="label__ribbon">Zested Over Korvale</p>
      <p class="label__volume">Nt. wt.1fl oz</p>
      <div class="label__rules label__rules--bottom"></div>
    </section>

    <section class="label label--olive">
      <div class="label__rules label__rules--top"></div>
      <div class="label__ginger-art" role="img" aria-label="Line illustration of a ginger root behind the name"></div>
      <h2 class="label__title"><span class="title-top">ZOK</span><span class="title-mid">Ginger</span><span class="title-bottom">Beer</span></h2>
      <p class="label__ribbon">Zested Over Korvale</p>
      <p class="label__volume">Nt. wt.1fl oz</p>
      <div class="label__rules label__rules--bottom"></div>
    </section>

    <section class="label label--brown">
      <div class="label__rules label__rules--top"></div>
      <div class="label__ginger-art" role="img" aria-label="Line illustration of a ginger root behind the name"></div>
      <h2 class="label__title"><span class="title-top">ZOK</span><span class="title-mid">Ginger</span><span class="title-bottom">Beer</span></h2>
      <p class="label__ribbon">Zested Over Korvale</p>
      <p class="label__volume">Nt. wt.1fl oz</p>
      <div class="label__rules label__rules--bottom"></div>
    </section>
  </main>
</body>
</html>
```